New Book Cover Design Project for book about Selling Blend

DetWe need a book cover (front, back, spine) for a new book entitled ‘Selling Blend’’ and subtitled “not 4Ps but what customers want” (inverted commas not to be part of the title and subtitle). The author is Malcolm Trevesby. The publisher is Lindenfold Press. The finished size of the paperback version will be 5" x 8" (127 x 203.2 mm). There will be paperback, hardback, and e-book versions. The final number of pages is expected to be in the region of 80 pages. Text for the back cover is in an attached document. At the bottom of the back cover should be publisher logo (rectangular) on the left and space for the ISBN bar code on the right. The design should be original and not include any stock images that have been created by someone else or may require obtaining a copyright licence to use. Symbols in common use and not copyrighted are probably ok. There are no required images, photographs or symbols except the publisher logo at the left bottom of the back cover. Spine lettering should be UK/US style with the top of the writing nearest the front cover. The designer is free to be creative using appropriate diagrams, symbols or abstract designs. A copy of the publisher logo is attached. Designers are assured that when evaluating designs absolutely no notice whatsoever is taken of a designer's Studio Hive ranking or status; We are completely output driven, so what matters is the design, not the ranking or status of the designer. In a similar way, designs are not evaluated as 'good' or 'bad' - the winning design will be chosen after review by a design review panel and is not decided arbitrarily by a single person. All submitted designs should be capable of effective copyright assignment. Designs submitted for consideration should include front cover, spine, and back cover.
Candidate Selling Blend words that can be included in designs, if the designer wishes, include: product, place, promotion, price, consumer, company objectives, participants, physical evidence, process of service assembly, battery life, usability, security, fashion, design, brand, appearance, health, obedience, sustainability, accessibility, value, idea, information operation, beliefs, vectors.

Target Market(s)

Academics, teachers, text book writers, and students concerned with marketing.

Industry/Entity Type

Education

Font styles to use
Serif

Requirements
Must have
• • Author on the front cover and the spine. Templates have been added to the brief for the cover with spine for a 80 page book. There are .indd and .pdf templates that can be used. the .indd and .pdf templates show where the ISBN blocks should go. The other .PDF templates have the ISBN in the wrong place (middle of the lower back cover) but have more information about the meanings of template markings. Bleeds - PLEASE NOTE - the cover printing is not exact - there is minor variation when the printers print the covers. Therefore do not have solid blocks of colour that go to the edges of the spine or spine and cover pages with different blocks of colour - solid blocks of colour may go round the spine folds a little bit! See the templates - they indicate the areas for possible printing imprecision. The ISBN numbers in the template file names are what will be used - perfect is for the paperback and case is for the hardback.
Nice to have
• • It is not necessary to have the subtitle on the spine. The final book size may not be 80 pages, therefore the spine width may change, but not by much. • Use only standard fonts.
Should not have
• • Ideally, stock images should not be used as we cannot control other uses of images created by other sources, thus potentially damaging the book branding. I don't like solid black cover or spine backgrounds.

```html
<!DOCTYPE html>
<html lang="en">
<head>
<meta charset="utf-8">
<title>Selling Blend – Cover Spread</title>
<link rel="stylesheet" href="https://fonts.googleapis.com/css2?family=Anton&family=Poppins:wght@300;400;700;800&family=Cabin:wght@400;700&display=swap">
<style>
  :root {
    --navy: #0c2d6b;
    --navy-deep: #082255;
    --navy-light: #1a4592;
    --white: #ffffff;
    --page: #ffffff;
  }
  * { margin: 0; padding: 0; box-sizing: border-box; }
  html, body {
    width: 829px; height: 1200px; overflow: hidden;
    background: var(--page);
  }
  .canvas { position: relative; width: 829px; height: 1200px; }
  .cover-spread {
    position: absolute; left: 0; top: 272px;
    width: 829px; height: 655px;
    background: var(--navy);
    color: var(--white);
    overflow: hidden;
  }
  .network-texture {
    position: absolute; inset: 0;
    background:
      linear-gradient(150deg, transparent 35%, rgba(8,34,85,0.55) 55%, transparent 70%),
      linear-gradient(200deg, transparent 45%, rgba(26,69,146,0.45) 65%, transparent 85%),
      linear-gradient(180deg, var(--navy) 0%, var(--navy) 40%, var(--navy-deep) 100%);
  }
  .svg-layer { position: absolute; inset: 0; }

  .back-subtitle {
    position: absolute; left: 0; width: 420px; top: 104px;
    text-align: center;
    font-family: "Poppins", sans-serif; font-weight: 400; font-size: 14.5px;
  }
  .back-blurb {
    position: absolute; left: 39px; width: 340px; top: 126px;
    font-family: "Cabin", sans-serif; font-size: 9.7px; line-height: 15.45px;
    text-align: justify; text-align-last: center;
  }
  .about-author {
    position: absolute; left: 39px; width: 340px; top: 403px;
    font-family: "Cabin", sans-serif; font-size: 9.7px; line-height: 15.45px;
  }
  .about-author h2 { font-size: 10.2px; font-weight: 700; }
  .publisher-mark {
    position: absolute; left: 39px; top: 570px;
    display: flex; align-items: center; gap: 7px;
    font-family: "Cabin", sans-serif; font-size: 15px; font-weight: 400;
  }
  .publisher-mark .square { width: 14px; height: 14px; background: var(--white); }
  .isbn-space {
    position: absolute; left: 227px; top: 530px; width: 159px; height: 96px;
    background: var(--white);
  }
  .spine-title, .spine-author {
    position: absolute; left: 405px;
    writing-mode: vertical-rl;
    font-family: "Poppins", sans-serif; font-weight: 800; font-size: 11px;
    line-height: 16px; letter-spacing: 0.2px;
  }
  .spine-title { top: 48px; }
  .spine-author { top: 479px; }
  .front-subtitle {
    position: absolute; left: 528px; width: 200px; top: 322px;
    list-style: none; text-align: center;
    font-family: "Poppins", sans-serif; font-weight: 400; font-size: 20px;
    line-height: 41.8px;
  }
</style>
</head>
<body>
<div class="canvas">
  <section class="cover-spread" aria-label="Selling Blend book cover: back, spine and front">
    <div class="network-texture" role="img" aria-label="Abstract low-poly network of connected points and facets in shades of navy"></div>

    <svg class="svg-layer" width="829" height="655" viewBox="0 0 829 655">
      <g fill="#ffffff">
        <text class="back-title" x="89" y="80" textLength="245" lengthAdjust="spacingAndGlyphs"
              font-family="Anton, sans-serif" font-size="36">SELLING BLEND</text>
        <text class="front-title-top" x="449" y="97" textLength="342" lengthAdjust="spacingAndGlyphs"
              font-family="Anton, sans-serif" font-size="67">SELLING</text>
        <text class="front-title-main" x="449" y="276" textLength="342" lengthAdjust="spacingAndGlyphs"
              font-family="Anton, sans-serif" font-size="206">BLEND</text>
        <text class="front-author" x="446" y="614" textLength="350" lengthAdjust="spacingAndGlyphs"
              font-family="Poppins, sans-serif" font-weight="800" font-size="36">MALCOLM TREVESBY</text>
      </g>
    </svg>

    <p class="back-subtitle">Not 4Ps But What Customers Want</p>
    <p class="back-blurb">This book has been inspired by the many textbooks, classes and student work about selling blend, which simply present or teach selling blend as 4Ps - very often not even acknowledging where those 4Ps came from. This approach is simply unacceptable academic work - no discussion of the extensive research from the 1920s onwards, about what is needed for effective marketing and selling blend. In several ways, this is a thoroughly radical book pushing against the common approach of simply teaching about simplistic 4Ps. Many students produce a selling blend for a company; they shouldn't. The book provides a solid example of what academics often call 'critical thinking'. Other ways in which the book is radical, is that it shows that selling blend is not only for products and services; it is also for ideas. The book discusses the idea that marketing can be seen as a branch of information warfare. Positioning should be included in selling blend considerations. Selling blend should not only be considered for legitimate products, services, and ideas; it is relevant also for those who trade in legal or mixed legal and illegal products and services. Examples are explored in the book.</p>
    <div class="about-author">
      <h2>About the Author:</h2>
      <p>Malcolm Trevesby has extensive experience in industry, academia, and a variety of NGOs working in human and civil rights. Within those contexts, he has a lot of marketing experience as practitioner, academic, and external examiner – contributing to the radical nature of this book.</p>
    </div>
    <div class="publisher-mark"><span class="square"></span><span>Lindenfold Press</span></div>
    <div class="isbn-space" aria-label="Space reserved for ISBN"></div>

    <p class="spine-title">SELLING BLEND</p>
    <p class="spine-author">MALCOLM TREVESBY</p>

    <ul class="front-subtitle">
      <li>NOT</li><li>4PS</li><li>BUT</li><li>WHAT</li><li>CUSTOMERS</li><li>WANT</li>
    </ul>
  </section>
</div>
</body>
</html>
```